Crestline Lending Group Business Cards

We are looking to revamp the current business cards each of our locations uses. We are a lending company that specializes in personal loans, title loans, and tax services. We have locations in New Mexico, Texas, and Oklahoma.

We would like a cleaner, sleeker look while still highlighting what we offer. Title Loans, Personal Loans & Tax Services. We also want to include our referral fee somewhere on the card. We would like to see an English option as well as a Spanish option for the cards.

PLEASE NOTE: Some business cards do not include the employee's name but just the store's location, while others will include both.

These are double-sided business cards, and we would like to see proof if possible. I have included proofs of our current business cards for you to review below, as well as our company logo. Feel free to get creative with the logo, etc! Colors should match the logo; however, you do not need to use all of our logo colors if you don't want to.

```html
<!DOCTYPE html>
<html lang="en">
<head>
<meta charset="utf-8">
<title>Crestline Lending Group Business Cards</title>
<link href="https://fonts.googleapis.com/css2?family=Poppins:wght@400;500;600&display=swap" rel="stylesheet">
<style>
  :root {
    --green: #0f4f2f;
    --green-box: #135c38;
    --red: #c8202c;
    --white: #ffffff;
    --backdrop: #efefec;
  }
  * { margin: 0; padding: 0; box-sizing: border-box; }
  html, body { width: 1200px; height: 1200px; overflow: hidden; }
  body {
    background: var(--backdrop);
    font-family: "Poppins", sans-serif;
    position: relative;
  }
  .card {
    position: absolute;
    left: 160px;
    width: 880px;
    height: 530px;
    overflow: hidden;
    box-shadow: 0 14px 30px rgba(0,0,0,0.18);
  }

  /* Back side */
  .card-back { top: 50px; background: var(--green); }
  .card-back .curve { position: absolute; left: 0; top: 0; }
  .brand-back {
    position: absolute;
    left: 0; right: 0; top: 205px;
    display: flex; align-items: center; justify-content: center; gap: 16px;
  }
  .brand-back .brand-dot {
    width: 22px; height: 22px; border-radius: 50%; background: var(--white);
  }
  .brand-back .brand-name {
    color: var(--white); font-size: 46px; font-weight: 500; letter-spacing: 0.5px;
  }
  .services {
    position: absolute; left: 0; right: 0; bottom: 26px;
    display: flex; justify-content: center; gap: 48px;
    list-style: none;
  }
  .services li {
    display: flex; align-items: center; gap: 10px;
    color: var(--green); font-size: 19px; font-weight: 500;
  }

  /* Front side */
  .card-front { top: 620px; background: var(--white); }
  .brand-front {
    position: absolute; left: 60px; top: 78px;
    display: flex; align-items: center; gap: 10px;
  }
  .brand-front .brand-dot {
    width: 14px; height: 14px; border-radius: 50%; background: var(--red);
  }
  .brand-front .brand-name {
    color: var(--green); font-size: 22px; font-weight: 600;
  }
  .referral {
    position: absolute; left: 72px; top: 210px;
    width: 241px; height: 320px;
    background: var(--green-box); color: var(--white);
    padding: 52px 0 0 26px;
  }
  .referral .refer-line { font-size: 27px; font-weight: 400; line-height: 1; }
  .referral .refer-line strong { font-weight: 600; }
  .referral .get-line {
    display: flex; align-items: center; gap: 8px; margin-top: 14px;
  }
  .referral .get {
    font-size: 70px; font-weight: 600; line-height: 0.9;
  }
  .referral .up-to {
    font-size: 30px; font-weight: 600; line-height: 0.95; display: flex; flex-direction: column;
  }
  .referral .amount { font-size: 78px; font-weight: 600; line-height: 1.1; margin-top: 2px; }

  .person { position: absolute; left: 542px; top: 90px; }
  .person .name { color: var(--green); font-size: 46px; font-weight: 600; line-height: 1; }
  .person .name span { font-weight: 400; }
  .person .role { color: var(--red); font-size: 19px; font-weight: 600; margin-top: 4px; }

  .contact-rail {
    position: absolute; left: 488px; top: 210px;
    width: 35px; height: 237px; border-radius: 18px;
    background: var(--red);
  }
  .contact-rail svg { position: absolute; left: 9px; }
  .contact-list {
    position: absolute; left: 556px; top: 228px;
    list-style: none; color: var(--green);
    font-size: 20px; font-weight: 500; line-height: 1.1;
  }
  .contact-list li { position: absolute; left: 0; white-space: nowrap; }
</style>
</head>
<body>

  <section class="card card-back" aria-label="Card back">
    <svg class="curve" width="880" height="530" viewBox="0 0 880 530">
      <path d="M0,418 Q440,330 880,430 L880,530 L0,530 Z" fill="#c8202c"/>
      <path d="M0,434 Q440,350 880,448 L880,530 L0,530 Z" fill="#ffffff"/>
    </svg>
    <div class="brand-back">
      <span class="brand-dot"></span>
      <span class="brand-name">Crestline Lending Group</span>
    </div>
    <ul class="services">
      <li><svg width="16" height="16" viewBox="0 0 16 16"><circle cx="8" cy="8" r="6.5" fill="none" stroke="#c8202c" stroke-width="1.6"/><path d="M5 8.2l2.2 2.2L11.5 5.6" fill="none" stroke="#c8202c" stroke-width="1.6"/></svg>Title Loans</li>
      <li><svg width="16" height="16" viewBox="0 0 16 16"><circle cx="8" cy="8" r="6.5" fill="none" stroke="#c8202c" stroke-width="1.6"/><path d="M5 8.2l2.2 2.2L11.5 5.6" fill="none" stroke="#c8202c" stroke-width="1.6"/></svg>Personal Loans</li>
      <li><svg width="16" height="16" viewBox="0 0 16 16"><circle cx="8" cy="8" r="6.5" fill="none" stroke="#c8202c" stroke-width="1.6"/><path d="M5 8.2l2.2 2.2L11.5 5.6" fill="none" stroke="#c8202c" stroke-width="1.6"/></svg>Tax Services</li>
    </ul>
  </section>

  <section class="card card-front" aria-label="Card front">
    <div class="brand-front">
      <span class="brand-dot"></span>
      <span class="brand-name">Crestline Lending Group</span>
    </div>

    <div class="referral">
      <p class="refer-line"><strong>Refer</strong> a Friend</p>
      <div class="get-line">
        <span class="get">GET</span>
        <span class="up-to"><span>up</span><span>to</span></span>
      </div>
      <p class="amount">$100</p>
    </div>

    <div class="person">
      <p class="name">Jane <span>Doe</span></p>
      <p class="role">Branch Manager</p>
    </div>

    <div class="contact-rail">
      <svg style="top:14px" width="17" height="17" viewBox="0 0 16 16"><path d="M8 1.5a4.5 4.5 0 0 0-4.5 4.5c0 3.3 4.5 8.5 4.5 8.5s4.5-5.2 4.5-8.5A4.5 4.5 0 0 0 8 1.5z" fill="#fff"/><circle cx="8" cy="6" r="1.6" fill="#c8202c"/></svg>
      <svg style="top:90px" width="17" height="17" viewBox="0 0 16 16"><path d="M4 1.8l2.2 2.6-1.2 1.7c.8 1.8 2.1 3.1 3.9 3.9l1.7-1.2 2.6 2.2-1.2 2.2C7.5 13 3 8.5 1.8 4.2z" fill="#fff"/></svg>
      <svg style="top:146px" width="17" height="17" viewBox="0 0 16 16"><rect x="1.5" y="3.5" width="13" height="9" rx="1" fill="#fff"/><path d="M2 4.2l6 4.5 6-4.5" fill="none" stroke="#c8202c" stroke-width="1.2"/></svg>
      <svg style="top:196px" width="17" height="17" viewBox="0 0 16 16"><circle cx="8" cy="8" r="6.2" fill="none" stroke="#fff" stroke-width="1.5"/><ellipse cx="8" cy="8" rx="2.6" ry="6.2" fill="none" stroke="#fff" stroke-width="1.3"/><path d="M2 8h12" stroke="#fff" stroke-width="1.3"/></svg>
    </div>

    <ul class="contact-list">
      <li style="top:0">123 Elm Street, Suite B,<br>Anytown, Texas 55555</li>
      <li style="top:70px">(505) 555-1212</li>
      <li style="top:124px">abcde@crestlinelending.com</li>
      <li style="top:173px">www.crestlinelending.com</li>
    </ul>
  </section>

</body>
</html>
```